Car finance company business card

Create a nice business card for our car financing company , Visit our website www.brookmilefinance.com for the phone number and idea of the company look. Please do not be afraid to be creative. Name on card Is Marc-Olivier Dussault and phone number is on our website adress of business is
27816 Boulevard Des-Ormeaux,
Mirabel, QC H4R 2B6

```html
<!DOCTYPE html>
<html lang="en">
<head>
<meta charset="utf-8">
<title>Brookmile Finance – Business Card</title>
<link rel="stylesheet" href="https://fonts.googleapis.com/css2?family=Roboto:wght@400;500&family=Roboto+Condensed:wght@700&display=swap">
<style>
  :root {
    --backdrop: #3b3b3d;
    --card: #2a2a2c;
    --orange: #e8702a;
    --blue: #5a66c8;
    --purple: #6a4fb0;
    --white: #f2f2f2;
    --muted: #b5b5b5;
    --mascot-orange: #d9662a;
  }
  * { margin: 0; padding: 0; box-sizing: border-box; }
  html, body { width: 799px; height: 1200px; overflow: hidden; }
  body {
    background: var(--backdrop);
    font-family: "Roboto", Arial, sans-serif;
    position: relative;
  }
  .card {
    position: absolute;
    left: 80px;
    width: 640px;
    height: 366px;
    border-radius: 22px;
    background: var(--card);
    overflow: hidden;
    box-shadow: 0 14px 30px rgba(0,0,0,.45);
  }
  .card--front { top: 110px; }
  .card--back { top: 720px; }

  /* front */
  .front__decor {
    position: absolute; left: 0; top: 0; width: 300px; height: 300px;
    background: radial-gradient(circle at 40% 40%, rgba(140,70,30,.22), rgba(42,42,44,0) 70%);
  }
  .brand {
    position: absolute;
    font-family: "Roboto Condensed", Arial, sans-serif;
    font-weight: 700;
    color: var(--white);
    text-transform: uppercase;
    line-height: 1;
    letter-spacing: 1px;
  }
  .front__brand { left: 170px; top: 110px; font-size: 46px; width: 330px; text-align: center; }
  .front__brand .brand__sub { display: block; font-size: 28px; margin-top: 6px; }
  .mascot {
    position: absolute;
    border-radius: 40% 40% 30% 30%;
    background: linear-gradient(160deg, var(--mascot-orange), #4a4fa0);
  }
  .front__mascot { left: 480px; top: 70px; width: 110px; height: 170px; }
  .front__rule { position: absolute; top: 262px; height: 3px; }
  .front__rule--left { left: 150px; width: 120px; background: var(--orange); }
  .front__rule--mid { left: 270px; width: 150px; background: var(--blue); }
  .front__rule--right { left: 420px; width: 80px; background: var(--orange); }
  .front__web {
    position: absolute; left: 0; width: 640px; top: 236px;
    text-align: center; color: var(--white); font-size: 17px;
  }
  .front__edge { position: absolute; bottom: 0; height: 5px; }
  .front__edge--orange { left: 0; width: 320px; background: var(--orange); }
  .front__edge--blue { left: 320px; width: 320px; background: var(--blue); }

  /* back */
  .back__wave { position: absolute; left: 0; top: 0; width: 640px; height: 366px; }
  .back__mascot { left: 34px; top: 18px; width: 100px; height: 112px; }
  .back__brand { left: 150px; top: 40px; font-size: 50px; }
  .back__brand .brand__sub { display: block; font-size: 26px; margin-top: 4px; padding-left: 40px; }
  .back__name {
    position: absolute; left: 34px; top: 146px;
    font-family: "Roboto Condensed", Arial, sans-serif; font-weight: 700;
    font-size: 22px; line-height: 26px; color: var(--orange);
  }
  .back__title { position: absolute; left: 34px; top: 174px; font-size: 14px; line-height: 18px; color: var(--muted); }
  .contact {
    position: absolute; right: 24px; top: 250px;
    list-style: none; color: var(--white); font-size: 17px; text-align: right;
  }
  .contact li { display: flex; justify-content: flex-end; align-items: center; gap: 8px; height: 21px; }
  .contact svg { width: 14px; height: 14px; fill: var(--card); }
  .contact .no-icon { padding-right: 22px; }
</style>
</head>
<body>
  <section class="card card--front">
    <div class="front__decor" role="img" aria-label="Faint mascot decoration"></div>
    <div class="brand front__brand">Brookmile<span class="brand__sub">Finance</span></div>
    <div class="mascot front__mascot" role="img" aria-label="Cartoon fox mascot holding car keys"></div>
    <p class="front__web">www.brookmilefinance.com</p>
    <div class="front__rule front__rule--left"></div>
    <div class="front__rule front__rule--mid"></div>
    <div class="front__rule front__rule--right"></div>
    <div class="front__edge front__edge--orange"></div>
    <div class="front__edge front__edge--blue"></div>
  </section>

  <section class="card card--back">
    <svg class="back__wave" viewBox="0 0 640 366" aria-hidden="true">
      <path d="M0 228 C120 234 200 262 320 262 C450 262 560 220 640 200 L640 366 L0 366 Z" fill="var(--orange)"/>
      <path d="M0 212 C120 218 200 246 320 246 C450 246 560 204 640 184 L640 193 C560 213 450 255 320 255 C200 255 120 227 0 221 Z" fill="var(--purple)"/>
      <path d="M0 202 C70 204 130 214 190 232 C130 220 70 214 0 213 Z" fill="var(--blue)"/>
    </svg>
    <div class="mascot back__mascot" role="img" aria-label="Cartoon fox mascot giving a thumbs up"></div>
    <div class="brand back__brand">Brookmile<span class="brand__sub">Finance</span></div>
    <p class="back__name">Marc-Olivier Dussault</p>
    <p class="back__title">Managing Director</p>
    <ul class="contact">
      <li>(514) 555-0182
        <svg viewBox="0 0 16 16"><path d="M3 1h3l1.5 4-2 1.2a9 9 0 0 0 4.3 4.3L11 8.5l4 1.5v3a2 2 0 0 1-2 2A12 12 0 0 1 1 3a2 2 0 0 1 2-2z"/></svg></li>
      <li>brookmilefinance.com
        <svg viewBox="0 0 16 16"><circle cx="8" cy="8" r="7"/></svg></li>
      <li>info@brookmilefinance.com
        <svg viewBox="0 0 16 16"><path d="M1 3h14v10H1z"/></svg></li>
      <li class="no-icon">27816 Boulevard Des-Ormeaux</li>
      <li class="no-icon">Mirabel, QC H4R 2B6</li>
    </ul>
  </section>
</body>
</html>
```